Brasko Construction Business Card

I need a business card design for my company.
We are a construction/machinery company.
I would like to see my logo on the front of the card and my details on the other side
I would like the card to be black or dark grey in colour,with my logo as i send it or modified with a lighter blue colour
I would like to see the design kept fairly simple,but eye catching at the same time
Industry/Entity Type
Business
Contact Information for Business Card
Name
Phone Number
Address
Email
Colors
00a990
1b1b1b
000000
474747
ececec

```html
<!DOCTYPE html>
<html lang="en">
<head>
<meta charset="UTF-8">
<title>Brasko Construction Business Card</title>
<link rel="stylesheet" href="https://fonts.googleapis.com/css2?family=Didact+Gothic&display=swap">
<style>
  :root {
    --teal: #00a990;
    --card: #1b1b1b;
    --black: #000000;
    --mid-grey: #474747;
    --light: #ececec;
    --muted: #a8a8a8;
    --stage: #d4d4d4;
  }
  * { margin: 0; padding: 0; box-sizing: border-box; }
  html, body {
    width: 1200px; height: 900px; overflow: hidden;
    background: var(--stage);
    font-family: "Didact Gothic", sans-serif;
    color: var(--light);
  }
  .canvas { position: relative; width: 1200px; height: 900px; }
  .card {
    position: absolute;
    width: 560px; height: 320px;
    background: var(--card);
    border-radius: 22px;
    box-shadow: 0 8px 22px rgba(0,0,0,0.35);
    overflow: hidden;
  }
  .card-front { left: 140px; top: 90px; }
  .card-back { left: 500px; top: 470px; }

  /* Front */
  .brand {
    position: absolute; inset: 0;
    display: flex; align-items: center; justify-content: center; gap: 16px;
  }
  .brand-mark { width: 30px; height: 30px; background: var(--teal); flex: none; }
  .brand-name {
    font-size: 34px; letter-spacing: 3px; text-transform: uppercase;
    color: var(--light); white-space: nowrap;
  }

  /* Back */
  .machinery-art {
    position: absolute; left: 40px; top: 10px; width: 340px; height: 190px;
    background: radial-gradient(closest-side, rgba(236,236,236,0.10) 0%, rgba(236,236,236,0.05) 55%, rgba(236,236,236,0) 100%);
  }
  .person {
    position: absolute; right: 34px; top: 26px; text-align: right;
  }
  .person-name { font-size: 24px; letter-spacing: 1px; color: var(--light); }
  .person-role { font-size: 12px; color: var(--muted); margin-top: 2px; }
  .rule-top {
    position: absolute; left: 260px; right: 20px; top: 192px;
    height: 1px; background: var(--teal);
  }
  .contacts {
    position: absolute; left: 24px; bottom: 20px; list-style: none;
  }
  .contact {
    display: flex; align-items: center; gap: 10px;
    font-size: 14px; line-height: 20px; color: var(--light);
    white-space: nowrap;
  }
  .contact svg { width: 12px; height: 12px; fill: var(--teal); flex: none; }
  .contact svg .cut { fill: var(--card); }
  .contact svg .cut-line { stroke: var(--card); fill: none; }
  .address-line {
    position: absolute; left: 340px; right: 20px; bottom: 29px;
    height: 1px; background: var(--teal);
  }
</style>
</head>
<body>
<main class="canvas">
  <section class="card card-front" aria-label="Card front">
    <div class="brand">
      <span class="brand-mark"></span>
      <span class="brand-name">Brasko Construction</span>
    </div>
  </section>

  <section class="card card-back" aria-label="Card back">
    <div class="machinery-art" role="img" aria-label="Faint excavator arm and bucket illustration"></div>
    <div class="person">
      <div class="person-name">MARK ELLISON</div>
      <div class="person-role">Director</div>
    </div>
    <div class="rule-top"></div>
    <ul class="contacts">
      <li class="contact">
        <svg viewBox="0 0 12 12" aria-hidden="true"><rect x="3" y="0" width="6" height="12" rx="1"/><rect class="cut" x="4" y="1.5" width="4" height="6"/></svg>
        <span>+630-555-0182</span>
      </li>
      <li class="contact">
        <svg viewBox="0 0 12 12" aria-hidden="true"><path d="M1 4 Q6 0 11 4 L9 5.5 L8 4 Q6 3.4 4 4 L3 5.5 Z"/><rect x="2" y="6" width="8" height="5" rx="1"/></svg>
        <span>+630-555-0182</span>
      </li>
      <li class="contact">
        <svg viewBox="0 0 12 12" aria-hidden="true"><rect x="0" y="2" width="12" height="8" rx="1"/><path class="cut-line" d="M1 3 L6 7 L11 3" stroke-width="1"/></svg>
        <span>mark@braskoconstruction.com</span>
      </li>
      <li class="contact">
        <svg viewBox="0 0 12 12" aria-hidden="true"><circle cx="6" cy="6" r="6"/><path class="cut-line" d="M0.5 6 H11.5 M6 0.5 V11.5" stroke-width="0.9"/></svg>
        <span>www.braskoconstruction.com</span>
      </li>
      <li class="contact">
        <svg viewBox="0 0 12 12" aria-hidden="true"><path d="M6 0.5 L12 6 H10 V11.5 H7.5 V8 H4.5 V11.5 H2 V6 H0 Z"/></svg>
        <span>Maison Claire 12 rue des Ormes france</span>
      </li>
    </ul>
    <div class="address-line"></div>
  </section>
</main>
</body>
</html>
```